Company Introduction/Advertisement Flyer

We would like to redesign our current company line card. We send this printed flyer to prospective customers to introduce our company, the brands we represent and our competitive advantages. Our current design is very plain and simple, we'd like to have a little more design to the new version. Our website is www.valvequarryhub.com. We're a specialty supplier for plumbing material, specifically water and life safety products. Our customers are mostly male, blue-collar contractors, ages 40-60. I have included a pdf of our current flyer, and our high resolution transparent logo.

Requirements
Must have
• Phone number: (800) 314-2760
Website: www.valvequarryhub.com

```html
<!DOCTYPE html>
<html lang="en">
<head>
<meta charset="utf-8">
<title>Valve Quarry Hub Flyer</title>
<link href="https://fonts.googleapis.com/css2?family=Noto+Sans:wght@400;600;700&display=swap" rel="stylesheet">
<style>
  :root {
    --navy: #10206e;
    --brand-blue: #1d57a8;
    --accent-red: #8c0a0a;
    --ink: #111111;
    --paper: #ffffff;
    --stage: #e2e2e2;
    --overlay: rgba(0, 0, 0, 0.82);
  }
  * { margin: 0; padding: 0; box-sizing: border-box; }
  html, body { width: 1200px; height: 1200px; overflow: hidden; }
  body { background: var(--stage); font-family: "Noto Sans", sans-serif; position: relative; }

  .flyer { position: absolute; left: 179px; top: 27px; width: 814px; height: 1152px; background: var(--paper); overflow: hidden; }
  .band-top { position: absolute; left: 0; top: 0; width: 814px; height: 56px; background: var(--navy); }
  .band-side { position: absolute; left: 0; top: 0; width: 47px; height: 489px; background: var(--navy); }

  .hero-photo { position: absolute; left: 47px; top: 56px; width: 767px; height: 521px;
    background: radial-gradient(ellipse at 55% 60%, #8a8a8a 0%, #4a4a4a 45%, #1e1e1e 100%); }

  .hero-caption { position: absolute; left: 55px; top: 419px; width: 759px; height: 146px; background: var(--overlay); color: #fff; text-align: right; padding-right: 44px; }
  .hero-title { font-weight: 700; font-size: 52px; line-height: 1; margin-top: 12px; letter-spacing: 0.5px; }
  .hero-offer { font-size: 26px; line-height: 35px; margin-top: 4px; }
  .hero-offer span + span { margin-left: 30px; }

  .perks { position: absolute; left: 100px; top: 606px; list-style: none; }
  .perks li { position: relative; padding-left: 35px; font-size: 24px; line-height: 28px; color: var(--ink); margin-bottom: 13px; }
  .perks li::before { content: ""; position: absolute; left: 2px; top: 8px; width: 13px; height: 13px; background: var(--accent-red); transform: rotate(45deg); }
  .perks li.two-line::before { top: 22px; }

  .call { position: absolute; left: 233px; top: 942px; color: var(--accent-red); font-weight: 700; }
  .call-label { font-size: 20px; line-height: 22px; padding-left: 6px; }
  .call-number { font-size: 46px; line-height: 52px; }

  .brand { position: absolute; left: 50px; top: 1053px; display: flex; align-items: center; gap: 14px; color: var(--brand-blue); }
  .brand-square { width: 26px; height: 26px; background: var(--brand-blue); }
  .brand-name { font-size: 32px; line-height: 36px; }
  .brand-sub { font-size: 17px; line-height: 20px; }

  .contact { position: absolute; left: 499px; top: 1051px; color: var(--brand-blue); font-weight: 600; font-size: 21px; line-height: 32px; }
</style>
</head>
<body>
  <div class="flyer">
    <div class="band-top"></div>
    <div class="band-side"></div>
    <div class="hero-photo" role="img" aria-label="Black and white photo of a workbench covered with valve repair parts, seals, fittings and tools"></div>
    <div class="hero-caption">
      <h1 class="hero-title">Your Complete Source For</h1>
      <p class="hero-offer"><span>Backflow Preventer Repair Parts</span><span>Accessories</span></p>
      <p class="hero-offer"><span>Enclosures</span><span>Test Gauge Calibration</span></p>
    </div>
    <ul class="perks">
      <li class="two-line">Save gas and time by<br>receiving parts at your doorstep</li>
      <li>1-2 day delivery anywhere in the country</li>
      <li>Same day shipping</li>
      <li>No minimum orders</li>
      <li>Online tracking of your order</li>
      <li>Friendly, knowledgable staff</li>
      <li>Technicians available to answer questions</li>
    </ul>
    <div class="call">
      <p class="call-label">Call Now</p>
      <p class="call-number">(800) 314-2760</p>
    </div>
    <div class="brand">
      <div class="brand-square"></div>
      <div>
        <p class="brand-name">Valve Quarry Hub</p>
        <p class="brand-sub">Supply Company</p>
      </div>
    </div>
    <div class="contact">
      <p>Fax: (850) 314-2791</p>
      <p>www.valvequarryhub.com</p>
    </div>
  </div>
</body>
</html>
```